Microblading website contest - Make it colorful

Beauty salon focusing on microblading need a better website template. Please make a 1 page site mobile optimized and nicer layout with better color formulation. Would love interactive images in the site. You can use stock images and if approve we can pay for it.
Current site:
tessawynkelpeony.com

Inspiration:
https://framqueue.net/shots/41877260-Microblading-HomePage
https://framqueue.net/shots/7914026-Lunetto-Microblading-Eyebrow-Beauty-Salon-Pagewright-Theme

Target Market(s)

women

Industry/Entity Type

beauty salon

Number of Pages Required

1 page

Font styles to use
Serif
Decorative
Script

Requirements
Nice to have
• As pretty as possible

```html
<!DOCTYPE html>
<html lang="en">
<head>
<meta charset="utf-8">
<title>Peony Brow House – Homepage Options</title>
<link rel="stylesheet" href="https://fonts.googleapis.com/css2?family=Playfair+Display:wght@400;600&family=Montserrat:wght@400;600;700&display=swap">
<style>
:root{
  --ink:#1b1718;
  --ink-2:#262123;
  --pink:#d63a6a;
  --pink-soft:#f3c9d6;
  --maroon:#6e1a36;
  --paper:#ffffff;
  --mist:#f6f2f3;
  --grey:#8a8385;
  --line:#e4dcde;
  --photo-skin:linear-gradient(135deg,#caa08c,#6d4a3f);
  --photo-dark:linear-gradient(135deg,#3c3133,#131011);
  --photo-studio:linear-gradient(135deg,#d9cfc9,#7b6d68);
}
*{box-sizing:border-box;margin:0;padding:0}
html,body{width:1200px;height:2636px;overflow:hidden}
body{background:var(--paper);font-family:"Montserrat",sans-serif;color:var(--ink);position:relative}
.option-label{position:absolute;top:22px;width:460px;text-align:center;font:700 22px "Montserrat",sans-serif;letter-spacing:1px}
.option-label--one{left:100px}
.option-label--two{left:640px}
.page{position:absolute;top:140px;width:460px;height:2460px;box-shadow:0 0 0 1px var(--line);overflow:hidden}
.page--one{left:100px}
.page--two{left:640px}
.section{position:relative;overflow:hidden}
.photo{position:absolute;background:var(--photo-skin)}
.photo--dark{background:var(--photo-dark)}
.photo--studio{background:var(--photo-studio)}
.serif{font-family:"Playfair Display",serif;font-weight:400}
.eyebrow{font-size:5px;letter-spacing:1.5px;text-transform:uppercase;color:var(--pink)}
.copy{font-size:5px;line-height:8px;color:var(--grey)}
.btn{display:inline-block;font-size:5px;letter-spacing:1px;padding:5px 12px;border:1px solid currentColor;text-transform:uppercase}
.btn--solid{background:var(--pink);border-color:var(--pink);color:#fff}
/* hero */
.hero{height:332px;background:var(--ink);color:#fff}
.hero .photo{right:0;top:0;width:300px;height:332px;background:linear-gradient(90deg,var(--ink) 0%,#5a3b33 45%,#b98a73 100%)}
.hero__nav{position:absolute;top:12px;left:40px;right:20px;display:flex;justify-content:space-between;font-size:5px;z-index:2}
.hero__brand{font:600 7px "Playfair Display",serif}
.hero__menu span{margin-left:10px;opacity:.85}
.hero__text{position:absolute;left:40px;top:120px;z-index:2}
.hero__title{font-size:30px;line-height:34px}
.hero__sub{font-size:6px;margin:8px 0 14px;opacity:.8}
.sidebar{position:absolute;left:0;top:0;width:24px;height:332px;background:#fff;z-index:3;display:flex;flex-direction:column;align-items:center;padding-top:14px;gap:10px}
.sidebar i{display:block;width:8px;height:1px;background:var(--ink)}
.sidebar b{display:block;width:10px;height:10px;border:1px solid var(--ink)}
.page--one .hero__nav,.page--one .hero__text{left:44px}
/* welcome */
.welcome{height:368px;background:#fff;text-align:center}
.welcome__head{padding-top:34px}
.welcome__title{font-size:18px;margin:6px 0 8px}
.welcome .copy{width:300px;margin:0 auto}
.welcome__band{position:absolute;left:120px;top:310px;width:160px;height:12px;background:var(--pink)}
/* services */
.services{height:320px;background:var(--ink);color:#fff}
.services__title{position:absolute;left:40px;top:34px;font-size:18px}
.services .eyebrow{position:absolute;left:40px;top:26px}
.services__grid{position:absolute;left:40px;top:72px;width:380px;display:grid;grid-template-columns:repeat(3,1fr);grid-auto-rows:80px;gap:4px}
.tile{position:relative;background:var(--photo-skin)}
.tile--pink{background:var(--pink);display:flex;flex-direction:column;justify-content:center;align-items:center;text-align:center;padding:8px}
.tile--light{background:#fff;color:var(--ink);display:flex;flex-direction:column;justify-content:center;align-items:center;text-align:center;padding:8px}
.tile h4{font:600 6px "Montserrat",sans-serif;letter-spacing:1px;margin-bottom:4px}
.tile p{font-size:4.5px;line-height:7px;opacity:.85}
.services .btn{position:absolute;left:50%;transform:translateX(-50%);top:262px}
/* works */
.works{height:320px;background:#fff;text-align:center}
.works__title{font-size:18px;margin-top:6px}
.works .eyebrow{margin-top:30px;display:block}
.works__grid{position:absolute;left:30px;top:86px;width:400px;display:grid;grid-template-columns:repeat(4,1fr);grid-auto-rows:96px;gap:4px}
.works__grid div{background:var(--photo-studio)}
.works__grid div:nth-child(odd){background:var(--photo-dark)}
/* about */
.about{height:200px;background:var(--ink);color:#fff}
.page--two .about{background:var(--maroon)}
.about__frame{position:absolute;left:56px;top:24px;width:120px;height:150px;border:1px solid rgba(255,255,255,.5)}
.about .photo{left:46px;top:34px;width:120px;height:150px;background:linear-gradient(160deg,#f2dcd4,#b98c82)}
.about__text{position:absolute;left:210px;top:52px;width:210px}
.about__title{font-size:18px;margin-bottom:8px}
.about .copy{color:rgba(255,255,255,.7);margin-bottom:12px}
/* beauty */
.beauty{height:240px;background:#fff;text-align:center}
.beauty__title{font-size:16px;padding-top:36px}
.beauty__sub{font-size:5px;color:var(--grey);margin-top:6px}
.beauty__items{position:absolute;left:30px;right:30px;top:100px;display:flex;justify-content:space-between}
.feature{width:120px;text-align:left}
.feature svg{display:block;margin:0 auto 10px}
.feature h5{font:600 6px "Montserrat",sans-serif;color:var(--pink);margin-bottom:4px}
/* academy */
.academy{height:200px;background:linear-gradient(180deg,#2a2224,var(--ink));color:#fff;text-align:center}
.academy__title{font-size:18px;padding-top:26px}
.academy__cards{position:absolute;left:30px;right:30px;top:68px;display:flex;gap:8px}
.card{flex:1;position:relative;height:100px;background:var(--photo-studio)}
.card span{position:absolute;left:0;right:0;bottom:0;background:rgba(0,0,0,.6);font-size:5px;padding:5px;text-align:left}
/* reviews */
.reviews{height:192px;background:#fff}
.reviews .eyebrow{position:absolute;left:40px;top:24px}
.reviews__title{position:absolute;left:40px;top:32px;font-size:14px}
.reviews__list{position:absolute;left:40px;right:30px;top:72px;display:flex;gap:14px}
.review{flex:1}
.review__who{display:flex;align-items:center;gap:6px;margin-bottom:6px}
.review__avatar{width:18px;height:18px;border-radius:50%;background:var(--photo-skin)}
.review__name{font:600 5.5px "Montserrat",sans-serif}
.review__stars{font-size:5px;color:var(--pink)}
/* newsletter */
.newsletter{height:88px;background:#fff}
.newsletter__band{position:absolute;left:20px;right:20px;top:14px;height:62px;background:var(--pink);color:#fff;display:flex;align-items:center;padding:0 22px;gap:20px}
.newsletter__title{font-size:16px;width:120px}
.newsletter__title small{display:block;font:5px "Montserrat",sans-serif;letter-spacing:1px;text-transform:uppercase;opacity:.8}
.newsletter__field{flex:1;height:16px;background:#fff;border-radius:2px;font-size:5px;color:var(--grey);padding:5px 8px}
.newsletter .btn{background:var(--ink);border-color:var(--ink)}
/* footer */
.footer{height:200px;background:var(--ink);color:#fff}
.footer__cols{position:absolute;left:30px;right:30px;top:30px;display:flex;gap:20px}
.footer__col{flex:1}
.footer__brand{font:600 10px "Playfair Display",serif;margin-bottom:8px}
.footer h6{font:600 6px "Montserrat",sans-serif;color:var(--pink);margin-bottom:8px}
.footer li{list-style:none;font-size:5px;line-height:10px;color:rgba(255,255,255,.7)}
.footer .copy{color:rgba(255,255,255,.6)}
.footer__social{display:flex;gap:6px;margin-top:6px}
.footer__social i{width:12px;height:12px;border-radius:50%;border:1px solid rgba(255,255,255,.6)}
.footer__bar{position:absolute;left:30px;right:30px;bottom:16px;border-top:1px solid rgba(255,255,255,.15);padding-top:8px;font-size:4.5px;color:rgba(255,255,255,.5)}
.footer__top{position:absolute;right:0;bottom:0;width:22px;height:14px;background:var(--pink)}
</style>
</head>
<body>

<div class="option-label option-label--one">OPTION 1</div>
<div class="option-label option-label--two">OPTION 2</div>

<!-- ===== Option 1 ===== -->
<main class="page page--one">
  <section class="section hero">
    <nav class="sidebar"><b></b><i></i><i></i><i></i></nav>
    <div class="photo" role="img" aria-label="Brow artist shaping a client's eyebrows"></div>
    <div class="hero__nav"><span class="hero__brand">Peony Brow House</span><span class="hero__menu"><span>Home</span><span>Services</span><span>Works</span><span>About</span><span>Contact</span></span></div>
    <div class="hero__text">
      <h1 class="serif hero__title">Peony Brow House<br>Tessa</h1>
      <p class="hero__sub">Microblading and brow artistry for natural beauty</p>
      <span class="btn">Book now</span>
    </div>
  </section>

  <section class="section welcome">
    <div class="welcome__head">
      <p class="eyebrow">About the studio</p>
      <h2 class="serif welcome__title">Welcome to Peony Brow House</h2>
      <p class="copy">We craft soft, natural brows with gentle hands and careful detail. Each treatment is shaped to your face so you leave looking fresh and feeling confident every day.</p>
    </div>
    <div class="photo" style="left:90px;top:140px;width:190px;height:160px" role="img" aria-label="Close-up of a microblading treatment"></div>
    <div class="photo photo--studio" style="left:290px;top:190px;width:90px;height:100px" role="img" aria-label="Team of brow artists in the salon"></div>
    <div class="welcome__band"></div>
  </section>

  <section class="section services">
    <p class="eyebrow">What we do</p>
    <h2 class="serif services__title">Our Services</h2>
    <div class="services__grid">
      <div class="tile" role="img" aria-label="Eyebrow treatment photo"></div>
      <div class="tile tile--pink"><h4>MICROBLADING</h4><p>Fine hair strokes for full, natural brows.</p></div>
      <div class="tile tile--light"><h4>LASH LIFT</h4><p>Curled lashes that last for weeks.</p></div>
      <div class="tile tile--light"><h4>POWDER BROWS</h4><p>Soft shaded look with gentle depth.</p></div>
      <div class="tile" role="img" aria-label="Brow artist at work"></div>
      <div class="tile tile--pink"><h4>LIP BLUSH</h4><p>Subtle tint for fresh, even lips.</p></div>
    </div>
    <span class="btn">View all</span>
  </section>

  <section class="section works">
    <span class="eyebrow">Portfolio</span>
    <h2 class="serif works__title">Our Perfect Works</h2>
    <div class="works__grid" role="img" aria-label="Gallery of before and after brow results">
      <div></div><div></div><div></div><div></div><div></div><div></div><div></div><div></div>
    </div>
  </section>

  <section class="section about">
    <div class="about__frame"></div>
    <div class="photo" role="img" aria-label="Portrait of brow artist Tessa"></div>
    <div class="about__text">
      <h2 class="serif about__title">About Tessa</h2>
      <p class="copy">Tessa has shaped brows for over ten years. She blends art and care to give every client brows that suit them and feel like their own.</p>
      <span class="btn">Read more</span>
    </div>
  </section>

  <section class="section beauty">
    <h2 class="serif beauty__title">Your Eyebrows and Beauty</h2>
    <p class="beauty__sub">Let us take care of you</p>
    <div class="beauty__items">
      <div class="feature"><svg width="26" height="26" viewBox="0 0 26 26"><circle cx="13" cy="13" r="12" fill="none" stroke="#d63a6a"/><path d="M8 13l3 3 7-7" fill="none" stroke="#d63a6a" stroke-width="1.5"/></svg><h5>Permanent Microblading</h5><p class="copy">Long lasting brows that need little care each day.</p></div>
      <div class="feature"><svg width="26" height="26" viewBox="0 0 26 26"><circle cx="13" cy="13" r="12" fill="none" stroke="#d63a6a"/><path d="M8 13l3 3 7-7" fill="none" stroke="#d63a6a" stroke-width="1.5"/></svg><h5>Brow Consultation</h5><p class="copy">We plan the shape and tone with you first.</p></div>
      <div class="feature"><svg width="26" height="26" viewBox="0 0 26 26"><circle cx="13" cy="13" r="12" fill="none" stroke="#d63a6a"/><path d="M8 13l3 3 7-7" fill="none" stroke="#d63a6a" stroke-width="1.5"/></svg><h5>Touch Up Sessions</h5><p class="copy">Keep your brows crisp with easy follow ups.</p></div>
    </div>
  </section>

  <section class="section academy">
    <h2 class="serif academy__title">Academy</h2>
    <div class="academy__cards">
      <div class="card" role="img" aria-label="Students in a brow training class"><span>Microblading Course</span></div>
      <div class="card" role="img" aria-label="Trainer guiding a student"><span>Powder Brow Course</span></div>
      <div class="card" role="img" aria-label="Group of graduates"><span>Master Class</span></div>
    </div>
  </section>

  <section class="section reviews">
    <p class="eyebrow">Testimonials</p>
    <h2 class="serif reviews__title">What Our Clients Have to Say</h2>
    <div class="reviews__list">
      <div class="review"><div class="review__who"><i class="review__avatar"></i><div><p class="review__name">Mara Quill</p><p class="review__stars">★★★★★</p></div></div><p class="copy">My brows look so natural. I wake up ready every day.</p></div>
      <div class="review"><div class="review__who"><i class="review__avatar"></i><div><p class="review__name">Jo Ellery</p><p class="review__stars">★★★★★</p></div></div><p class="copy">Calm studio, gentle work and a lovely result.</p></div>
      <div class="review"><div class="review__who"><i class="review__avatar"></i><div><p class="review__name">Nina Vashti</p><p class="review__stars">★★★★★</p></div></div><p class="copy">Tessa listened and gave me the shape I wanted.</p></div>
    </div>
  </section>

  <section class="section newsletter">
    <div class="newsletter__band">
      <h3 class="serif newsletter__title"><small>Subscribe</small>Our newsletter</h3>
      <span class="newsletter__field">Your email address</span>
      <span class="btn">Sign up</span>
    </div>
  </section>

  <footer class="section footer">
    <div class="footer__cols">
      <div class="footer__col"><p class="footer__brand">Peony Brow House</p><p class="copy">Natural brows crafted with care in a calm studio.</p></div>
      <div class="footer__col"><h6>Links</h6><ul><li>Home</li><li>Services</li><li>Academy</li><li>Contact</li></ul></div>
      <div class="footer__col"><h6>Contact</h6><ul><li>tessawynkelpeony.com</li><li>Open Mon – Sat</li></ul><div class="footer__social"><i></i><i></i><i></i></div></div>
    </div>
    <p class="footer__bar">© Peony Brow House. All rights reserved.</p>
    <span class="footer__top"></span>
  </footer>
</main>

<!-- ===== Option 2 ===== -->
<main class="page page--two">
  <section class="section hero">
    <div class="photo" role="img" aria-label="Brow artist shaping a client's eyebrows"></div>
    <div class="hero__nav"><span class="hero__brand">Peony Brow House</span><span class="hero__menu"><span>Home</span><span>Services</span><span>Works</span><span>About</span><span>Contact</span></span></div>
    <div class="hero__text">
      <h1 class="serif hero__title">Peony Brow House<br>Tessa</h1>
      <p class="hero__sub">Microblading and brow artistry for natural beauty</p>
      <span class="btn">Book now</span>
    </div>
  </section>

  <section class="section welcome">
    <div class="welcome__head">
      <p class="eyebrow">About the studio</p>
      <h2 class="serif welcome__title">Welcome to Peony Brow House</h2>
      <p class="copy">We craft soft, natural brows with gentle hands and careful detail. Each treatment is shaped to your face so you leave looking fresh and feeling confident every day.</p>
    </div>
    <div class="photo" style="left:60px;top:140px;width:190px;height:160px" role="img" aria-label="Close-up of a microblading treatment"></div>
    <div class="photo photo--studio" style="left:258px;top:190px;width:80px;height:100px" role="img" aria-label="Team of brow artists in the salon"></div>
    <div class="photo" style="left:350px;top:110px;width:90px;height:240px;background:linear-gradient(180deg,#efe3de,#1f1a1b)" role="img" aria-label="Brow artist standing in black dress"></div>
    <div class="welcome__band" style="left:90px"></div>
  </section>

  <section class="section services">
    <p class="eyebrow">What we do</p>
    <h2 class="serif services__title">Our Services</h2>
    <div class="services__grid">
      <div class="tile" role="img" aria-label="Eyebrow treatment photo"></div>
      <div class="tile tile--pink"><h4>MICROBLADING</h4><p>Fine hair strokes for full, natural brows.</p></div>
      <div class="tile tile--light"><h4>LASH LIFT</h4><p>Curled lashes that last for weeks.</p></div>
      <div class="tile tile--light"><h4>POWDER BROWS</h4><p>Soft shaded look with gentle depth.</p></div>
      <div class="tile" role="img" aria-label="Brow artist at work"></div>
      <div class="tile tile--pink"><h4>LIP BLUSH</h4><p>Subtle tint for fresh, even lips.</p></div>
    </div>
    <span class="btn">View all</span>
  </section>

  <section class="section works">
    <span class="eyebrow">Portfolio</span>
    <h2 class="serif works__title">Our Perfect Works</h2>
    <div class="works__grid" role="img" aria-label="Gallery of before and after brow results">
      <div></div><div></div><div></div><div></div><div></div><div></div><div></div><div></div>
    </div>
  </section>

  <section class="section about">
    <div class="about__frame"></div>
    <div class="photo" role="img" aria-label="Portrait of brow artist Tessa"></div>
    <div class="about__text">
      <h2 class="serif about__title">About Tessa</h2>
      <p class="copy">Tessa has shaped brows for over ten years. She blends art and care to give every client brows that suit them and feel like their own.</p>
      <span class="btn">Read more</span>
    </div>
  </section>

  <section class="section beauty">
    <h2 class="serif beauty__title">Your Eyebrows and Beauty</h2>
    <p class="beauty__sub">Let us take care of you</p>
    <div class="beauty__items">
      <div class="feature"><svg width="26" height="26" viewBox="0 0 26 26"><circle cx="13" cy="13" r="12" fill="none" stroke="#d63a6a"/><path d="M8 13l3 3 7-7" fill="none" stroke="#d63a6a" stroke-width="1.5"/></svg><h5>Permanent Microblading</h5><p class="copy">Long lasting brows that need little care each day.</p></div>
      <div class="feature"><svg width="26" height="26" viewBox="0 0 26 26"><circle cx="13" cy="13" r="12" fill="none" stroke="#d63a6a"/><path d="M8 13l3 3 7-7" fill="none" stroke="#d63a6a" stroke-width="1.5"/></svg><h5>Brow Consultation</h5><p class="copy">We plan the shape and tone with you first.</p></div>
      <div class="feature"><svg width="26" height="26" viewBox="0 0 26 26"><circle cx="13" cy="13" r="12" fill="none" stroke="#d63a6a"/><path d="M8 13l3 3 7-7" fill="none" stroke="#d63a6a" stroke-width="1.5"/></svg><h5>Touch Up Sessions</h5><p class="copy">Keep your brows crisp with easy follow ups.</p></div>
    </div>
  </section>

  <section class="section academy">
    <h2 class="serif academy__title">Academy</h2>
    <div class="academy__cards">
      <div class="card" role="img" aria-label="Students in a brow training class"><span>Microblading Course</span></div>
      <div class="card" role="img" aria-label="Trainer guiding a student"><span>Powder Brow Course</span></div>
      <div class="card" role="img" aria-label="Group of graduates"><span>Master Class</span></div>
    </div>
  </section>

  <section class="section reviews">
    <p class="eyebrow">Testimonials</p>
    <h2 class="serif reviews__title">What Our Clients Have to Say</h2>
    <div class="reviews__list">
      <div class="review"><div class="review__who"><i class="review__avatar"></i><div><p class="review__name">Mara Quill</p><p class="review__stars">★★★★★</p></div></div><p class="copy">My brows look so natural. I wake up ready every day.</p></div>
      <div class="review"><div class="review__who"><i class="review__avatar"></i><div><p class="review__name">Jo Ellery</p><p class="review__stars">★★★★★</p></div></div><p class="copy">Calm studio, gentle work and a lovely result.</p></div>
      <div class="review"><div class="review__who"><i class="review__avatar"></i><div><p class="review__name">Nina Vashti</p><p class="review__stars">★★★★★</p></div></div><p class="copy">Tessa listened and gave me the shape I wanted.</p></div>
    </div>
  </section>

  <section class="section newsletter">
    <div class="newsletter__band">
      <h3 class="serif newsletter__title"><small>Subscribe</small>Our newsletter</h3>
      <span class="newsletter__field">Your email address</span>
      <span class="btn">Sign up</span>
    </div>
  </section>

  <footer class="section footer">
    <div class="footer__cols">
      <div class="footer__col"><p class="footer__brand">Peony Brow House</p><p class="copy">Natural brows crafted with care in a calm studio.</p></div>
      <div class="footer__col"><h6>Links</h6><ul><li>Home</li><li>Services</li><li>Academy</li><li>Contact</li></ul></div>
      <div class="footer__col"><h6>Contact</h6><ul><li>tessawynkelpeony.com</li><li>Open Mon – Sat</li></ul><div class="footer__social"><i></i><i></i><i></i></div></div>
    </div>
    <p class="footer__bar">© Peony Brow House. All rights reserved.</p>
    <span class="footer__top"></span>
  </footer>
</main>

</body>
</html>
```